Ink & Toner Postcards (Set of 3)

Postcard
Some Content:

Header Option: STOP Killing your Printer with
Inferior Cartridges

Header Option: STOP Spending TOO MUCH $$ on Cheap Toner Cartridges

Secondary Message" Save Money
with QUALITY Toner Cartridges

Points to Get Across:
Buy Fewer Cartridges, Generate Over 25% (+) Yield
Eliminate Toner Contamination and Reduce Jams
Ensure Top Quality Printing and Printer Reliability
Competitive Prices

To Order, Visit qelvonsupply.com

Special Volume & Bundling Pricing
Call 888-471-2265

Target Market(s)

Small Business Owners
Independent Pharmacies

Industry/Entity Type

Printer

Requirements
Must have
• Phone Number
Website Address
2nd Side B&W, Set Up For Mailing
Output: Adobe Acrobat 9 Document (*.pdf) (recommended)
and
Adobe Illustrator CS3 Artwork (*.ai) (recommended)
or
Adobe Photoshop CS3 Image (*.psd) (recommended)

Full Bleed Size
5.59" x 4.33"
142 x 110 mm
1677 x 1300 pixels

Document Trim Size
5.47" x 4.21"
139 x 107 mm
1642 x 1264 pixels

OR

Full Bleed Size
8.64" x 5.59"
219 x 142 mm
2592 x 1677 pixels

Document Trim Size
8.52" x 5.47"
216 x 139 mm
2556 x 1642 pixels
Should not have
• Too Much Wording, Need Impact of Messaging To Act

```html
<!DOCTYPE html>
<html lang="en">
<head>
<meta charset="utf-8">
<title>Qelvon Supply Postcard – Mailing Side</title>
<link rel="stylesheet" href="https://fonts.googleapis.com/css2?family=Arimo:wght@400;700&display=swap">
<style>
  :root {
    --paper: #ffffff;
    --ink: #111111;
    --rule: #222222;
  }
  * { margin: 0; padding: 0; box-sizing: border-box; }
  html, body {
    width: 1200px;
    height: 923px;
    overflow: hidden;
    background: var(--paper);
  }
  .postcard {
    position: relative;
    width: 1200px;
    height: 923px;
    background: var(--paper);
    font-family: "Arimo", Arial, sans-serif;
    color: var(--ink);
  }
  .divider {
    position: absolute;
    left: 589px;
    top: 10px;
    width: 12px;
    height: 900px;
  }
  .stamp-box {
    position: absolute;
    left: 1031px;
    top: 31px;
    width: 128px;
    height: 154px;
    border: 1.5px solid var(--ink);
    display: flex;
    align-items: center;
    justify-content: center;
    text-align: center;
    font-size: 31px;
    line-height: 1.4;
  }
  .address-lines {
    position: absolute;
    left: 642px;
    top: 0;
    width: 504px;
  }
  .address-line {
    position: absolute;
    left: 0;
    width: 504px;
    height: 0;
    border-top: 1.5px solid var(--rule);
  }
  .sender {
    position: absolute;
    left: 28px;
    top: 788px;
  }
  .sender-name {
    display: flex;
    align-items: center;
    gap: 14px;
    font-weight: 700;
    font-size: 25px;
    letter-spacing: -0.3px;
  }
  .sender-mark {
    width: 22px;
    height: 22px;
    border-radius: 50%;
    background: var(--ink);
    margin-left: 72px;
  }
  .sender-contact {
    margin-top: 16px;
    margin-left: 102px;
    font-size: 20px;
  }
</style>
</head>
<body>
  <main class="postcard">
    <svg class="divider" viewBox="0 0 12 900" aria-hidden="true">
      <line x1="6" y1="6" x2="6" y2="894" stroke="#111111" stroke-width="4.5" stroke-linecap="round" stroke-dasharray="0 8.6"/>
    </svg>

    <div class="stamp-box">Place<br>stamp<br>here</div>

    <div class="address-lines">
      <div class="address-line" style="top:395px"></div>
      <div class="address-line" style="top:501px"></div>
      <div class="address-line" style="top:610px"></div>
      <div class="address-line" style="top:714px"></div>
    </div>

    <div class="sender">
      <div class="sender-name"><span class="sender-mark"></span>Qelvon Supply, LLC.</div>
      <div class="sender-contact">qelvonsupply.com | 888-471-2265</div>
    </div>
  </main>
</body>
</html>
```